Labor Day Sale Website Banner For High End Jewelry Website

We need a banner for our website (brindlyx.com) for a Labor Day Sale. The banner should be a size 1187 × 400. I have included a few pieces of jewelry to be included in the banner (do not need to use all, can use just some). The banner should say:
"Labor Day Sale"
"Save 15% on Everything!"
Use Promo Code: HALCYON

Target Market(s)

Affluent Female Consumers

Industry/Entity Type

Jewelry

Colors

Designer to choose colors to be used in the design.

```html
<!DOCTYPE html>
<html lang="en">
<head>
<meta charset="utf-8">
<title>Labor Day Sale – brindlyx.com</title>
<link href="https://fonts.googleapis.com/css2?family=Open+Sans:wght@600&family=Crimson+Pro:wght@400&family=Noto+Serif&display=swap" rel="stylesheet">
<style>
  :root {
    --blush-light: #fbe3e3;
    --blush: #f6c9c9;
    --blush-deep: #efb3b5;
    --flag-navy: #2b3a67;
    --flag-white: #f4eef0;
    --flag-red: #c8354a;
    --headline-red: #8e0f14;
    --promo-grey: #9a8a88;
    --white: #ffffff;
    --gem-gold: #c99a2e;
    --gem-violet: #6a5aa8;
  }
  * { margin: 0; padding: 0; box-sizing: border-box; }
  html, body { width: 1200px; height: 404px; overflow: hidden; }
  .banner {
    position: relative;
    width: 1200px;
    height: 404px;
    overflow: hidden;
    background: radial-gradient(ellipse at 60% 45%, var(--blush-light) 0%, var(--blush) 55%, var(--blush-deep) 100%);
  }
  .flag-bands { position: absolute; left: 0; top: 0; }
  .event-title {
    position: absolute;
    left: 18px;
    top: 9px;
    font-family: "Open Sans", Arial, sans-serif;
    font-weight: 600;
    font-size: 76px;
    line-height: 77px;
    color: var(--white);
    letter-spacing: -2px;
    text-shadow: 2px 3px 4px rgba(0,0,0,0.45);
  }
  .offer {
    position: absolute;
    font-family: "Crimson Pro", Georgia, serif;
    font-weight: 400;
    font-variant-numeric: lining-nums;
    color: var(--headline-red);
    line-height: 1;
    white-space: nowrap;
  }
  .offer-save { left: 312px; top: 24px; font-size: 110px; }
  .offer-amount { left: 314px; top: 120px; font-size: 152px; }
  .offer-scope { left: 314px; top: 242px; font-size: 74px; }
  .offer-bang { left: 738px; top: 128px; font-size: 215px; }
  .promo-code {
    position: absolute;
    left: 316px;
    top: 341px;
    font-family: "Noto Serif", Georgia, serif;
    font-size: 29px;
    line-height: 1;
    color: var(--promo-grey);
    white-space: nowrap;
  }
  .product-photo { position: absolute; }
  .product-earrings {
    left: 604px; top: 24px; width: 262px; height: 146px;
    border-radius: 50%;
    background: radial-gradient(ellipse at center, var(--gem-violet) 0%, rgba(106,90,168,0.5) 55%, rgba(106,90,168,0) 75%);
  }
  .product-pendant {
    left: 872px; top: 8px; width: 296px; height: 396px;
    border-radius: 45% 45% 40% 40%;
    background: radial-gradient(ellipse at 50% 55%, #e8dcc0 0%, var(--gem-gold) 55%, rgba(201,154,46,0) 75%);
  }
</style>
</head>
<body>
<main class="banner">
  <svg class="flag-bands" width="340" height="404" viewBox="0 0 340 404" aria-hidden="true">
    <polygon points="0,0 158,0 24,404 0,404" fill="var(--flag-navy)"/>
    <polygon points="158,0 232,0 100,404 24,404" fill="var(--flag-white)"/>
    <polygon points="232,0 322,0 190,404 100,404" fill="var(--flag-red)"/>
  </svg>

  <h1 class="event-title">LABOR<br>DAY<br>SALE</h1>

  <div class="product-photo product-earrings" role="img" aria-label="Pair of flower earrings with violet, blue and pink sapphire petals around a diamond centre"></div>
  <div class="product-photo product-pendant" role="img" aria-label="Gold egg-shaped pendant set with moonstone cabochons and blue sapphire drops"></div>

  <p class="offer offer-save">Save</p>
  <p class="offer offer-amount">15%</p>
  <p class="offer offer-scope">on everything</p>
  <span class="offer offer-bang">!</span>

  <p class="promo-code">Use Promo Code: HALCYON</p>
</main>
</body>
</html>
```